Aged Care Home - TP

We need a website design for a homepage and a content page for an aged care home in Brisbane. I have attached a detailed design/content brief and their logo to be used in concepts. Also bear in mind this design will be skinned for Dot Net Nuke 4.8.2 so design needs to be used on this content management system.

The following elements are required in the design:

• Phone number will be featured in banner on each page 07 5281 6372

• An area for a large flash banner of rotating images on homepage

• Images need to reflect credibility, professionalism and caring (just use some example images for now as we’ll need to source some)

• Large logo in banner as well

• Some icons on homepage to include:

• Download Application Form

• Admission Kit

• Contact Us

```html
<!DOCTYPE html>
<html lang="en">
<head>
<meta charset="utf-8">
<title>The Tessa Porter Home</title>
<link rel="stylesheet" href="https://fonts.googleapis.com/css2?family=Jost:wght@400;500&display=swap">
<style>
  :root {
    --sky-edge: #b3def0;
    --sky-mid: #e6f4fa;
    --page: #ffffff;
    --brand-blue: #1c28a8;
    --navy: #1b1f6e;
    --nav-top: #2a2f80;
    --nav-bottom: #0c0f48;
    --green-top: #8fd43c;
    --green-bottom: #66bb08;
    --lavender: #a9a4ec;
    --text: #1e1e1e;
    --hero-dark: #4d6b2c;
    --hero-light: #a6d36a;
  }
  * { box-sizing: border-box; margin: 0; padding: 0; }
  html, body { width: 1200px; height: 999px; overflow: hidden; }
  body {
    font-family: "Jost", sans-serif;
    background: linear-gradient(90deg, var(--sky-edge) 0%, var(--sky-mid) 45%, var(--sky-mid) 55%, var(--sky-edge) 100%);
    position: relative;
  }
  .page {
    position: absolute; left: 113px; top: 74px;
    width: 975px; height: 850px;
    background: var(--page);
  }
  .brand {
    position: absolute; left: 38px; top: 50px;
    display: flex; align-items: center; gap: 14px;
  }
  .brand-mark {
    width: 48px; height: 48px; border-radius: 50%;
    background: var(--lavender);
  }
  .brand-name {
    font-size: 24px; font-weight: 400; color: var(--brand-blue);
    letter-spacing: 0.5px;
  }
  .callout {
    position: absolute; right: 42px; top: 46px;
    color: var(--navy); font-size: 18px; line-height: 25px;
    letter-spacing: 0.6px;
  }
  .hero {
    position: absolute; left: 37px; top: 166px;
    width: 901px; height: 300px;
    background: linear-gradient(90deg, var(--hero-dark) 0%, #8a9f62 30%, var(--hero-light) 55%, #6f9a3c 80%, var(--hero-dark) 100%);
  }
  .main-nav {
    position: absolute; left: 37px; top: 466px;
    width: 901px; height: 50px;
    background: linear-gradient(180deg, var(--nav-top), var(--nav-bottom));
    border-radius: 0 0 12px 12px;
    display: flex; align-items: center; padding-left: 37px; gap: 21px;
  }
  .main-nav a {
    color: #fff; text-decoration: none; font-size: 15px; letter-spacing: 0.8px;
  }
  .quick-links {
    position: absolute; left: 39px; top: 553px;
    display: flex; flex-direction: column; gap: 23px;
  }
  .quick-link {
    width: 230px; height: 55px; border-radius: 9px;
    background: linear-gradient(180deg, var(--green-top), var(--green-bottom));
    display: flex; align-items: center; position: relative;
    color: #fff; text-decoration: none; font-size: 16px; letter-spacing: 0.8px; line-height: 20px;
  }
  .quick-link svg { position: absolute; left: 20px; top: 50%; transform: translateY(-50%); }
  .quick-link span { width: 100%; text-align: center; padding-left: 40px; }
  .intro {
    position: absolute; left: 305px; top: 545px; width: 640px;
    color: var(--text); font-size: 17px; line-height: 33px; letter-spacing: 0.6px;
  }
  .intro p + p { margin-top: 33px; }
</style>
</head>
<body>
  <div class="page">
    <header>
      <div class="brand">
        <div class="brand-mark"></div>
        <div class="brand-name">THE TESSA PORTER HOME</div>
      </div>
      <div class="callout">Call Us Today:<br>07 5281 6372</div>
    </header>

    <div class="hero" role="img" aria-label="Rotating banner: a young woman hugging an older woman, and an elderly couple on a park bench among green trees"></div>

    <nav class="main-nav">
      <a href="#">Home</a>
      <a href="#">About Us</a>
      <a href="#">Accommodation</a>
      <a href="#">Contact Us</a>
      <a href="#">Financial Info</a>
      <a href="#">Philosophy of Care</a>
      <a href="#">Sign up for newsletter</a>
    </nav>

    <div class="quick-links">
      <a class="quick-link" href="#">
        <svg width="24" height="30" viewBox="0 0 24 30"><rect x="1" y="1" width="22" height="28" fill="#fff"/><g stroke="#1b1f6e" stroke-width="2"><line x1="5" y1="8" x2="19" y2="8"/><line x1="5" y1="13" x2="19" y2="13"/><line x1="5" y1="18" x2="19" y2="18"/><line x1="5" y1="23" x2="19" y2="23"/></g></svg>
        <span>Download<br>Application Form</span>
      </a>
      <a class="quick-link" href="#">
        <svg width="30" height="26" viewBox="0 0 30 26"><path d="M1 2h10l2 3h16v20H1z" fill="#1b1f6e"/><rect x="1" y="6" width="28" height="19" fill="#fff"/></svg>
        <span>Admission Kit</span>
      </a>
      <a class="quick-link" href="#">
        <svg width="26" height="30" viewBox="0 0 26 30"><path d="M6 1c2 0 4 5 4 7s-3 3-3 4c0 3 5 10 8 11 1 0 2-3 4-3s6 3 6 5-3 4-5 4C10 29 1 15 1 6c0-3 3-5 5-5z" fill="#fff"/></svg>
        <span>Contact Us</span>
      </a>
    </div>

    <main class="intro">
      <p>We are an Aged Care Facility that has been providing quality care and accommodation to the Brisbane community for over twenty years.</p>
      <p>From this site you can learn more about us, find out all the types of accommodation available, what our Philosophy of Care is, send a message to a resident, contact us to request more information or download a brochure or an application form.</p>
    </main>
  </div>
</body>
</html>
```